Business Card design for an International Import Export House

We need a Business Card design for our import export business. We trade in Minerals, Metals, Rice, Sugar, Steel etc.. The design should be minimalistic. It may or may not contain the physical address. In case you want to include the physical address - 418 Verandah Heights, Marlow Sector 9, Dunmore, Kestrel State, 560417.

Target Market(s)

Steel Mills or Steel Plants, Factories, Mining businesses, Industrial houses, Government Agencies

Industry/Entity Type

Importer

Contact Information for Business Card

Business Name - Tessan Overseas

Font styles to use
Other font styles liked:
• montserrat

Requirements
Must have
• Ravi Kandola - President
• www.tessanoverseas.com
• ravi@tessanoverseas.com
• +91-987-654-3217
Nice to have
• global traders of minerals

```html
<!DOCTYPE html>
<html lang="en">
<head>
<meta charset="utf-8">
<title>Tessan Overseas — Business Card</title>
<link href="https://fonts.googleapis.com/css2?family=Montserrat:wght@600;700&family=Roboto:wght@400;500&display=swap" rel="stylesheet">
<style>
  :root {
    --backdrop: #5b4a3b;
    --paper: #ffffff;
    --ink: #1c1f22;
    --ink-soft: #4a4d50;
    --teal: #3f8fa9;
    --night: #1a1d20;
  }
  html, body {
    margin: 0;
    padding: 0;
    width: 1200px;
    height: 987px;
    overflow: hidden;
    background: var(--backdrop);
  }
  .canvas {
    position: relative;
    width: 1200px;
    height: 987px;
    font-family: "Roboto", Arial, sans-serif;
  }
  .card {
    position: absolute;
    left: 293px;
    width: 615px;
    height: 352px;
    box-shadow: 0 2px 6px rgba(0,0,0,0.35);
  }
  .card--front { top: 130px; background: var(--paper); }
  .card--back  { top: 505px; background: var(--night); }

  .holder-name {
    position: absolute;
    left: 39px;
    top: 48px;
    margin: 0;
    font-size: 21px;
    font-weight: 500;
    letter-spacing: 0.3px;
    color: var(--teal);
  }
  .holder-title {
    position: absolute;
    left: 39px;
    top: 74px;
    margin: 0;
    font-size: 16px;
    color: var(--ink);
  }
  .address {
    position: absolute;
    left: 39px;
    top: 153px;
    margin: 0;
    font-size: 15px;
    line-height: 20.5px;
    color: var(--ink-soft);
    font-style: normal;
  }
  .contact {
    position: absolute;
    left: 39px;
    top: 230px;
    margin: 0;
    padding: 0;
    list-style: none;
    font-size: 15px;
    line-height: 24px;
    color: var(--ink-soft);
  }
  .contact b { color: var(--teal); font-weight: 500; margin-right: 4px; }

  .web-band {
    position: absolute;
    left: 0;
    right: 0;
    top: 308px;
    height: 28px;
    background: var(--teal);
    border-top: 2px solid var(--paper);
    border-bottom: 2px solid var(--paper);
    box-shadow: 0 -2px 0 var(--teal), 0 2px 0 var(--teal);
    color: #fff;
    font-size: 14px;
    letter-spacing: 3.4px;
    line-height: 28px;
    padding-left: 35px;
    box-sizing: content-box;
  }

  .brand {
    position: absolute;
    top: 75px;
    display: flex;
    flex-direction: column;
    align-items: center;
    font-family: "Montserrat", Arial, sans-serif;
    font-weight: 700;
    letter-spacing: -0.5px;
    line-height: 28px;
    white-space: nowrap;
    transform: translateX(-50%);
  }
  .brand-dot {
    border-radius: 50%;
    border: 3px solid var(--teal);
    box-sizing: border-box;
  }
  .brand--front {
    left: 469px;
    gap: 40px;
    font-size: 23px;
    color: var(--ink);
  }
  .brand--front .brand-dot { width: 130px; height: 130px; }
  .brand--back {
    left: 50%;
    gap: 52px;
    font-size: 25px;
    color: #ffffff;
  }
  .brand--back .brand-dot { width: 150px; height: 150px; }
</style>
</head>
<body>
<main class="canvas">
  <section class="card card--front" aria-label="Business card front">
    <h1 class="holder-name">RAVI KANDOLA</h1>
    <p class="holder-title">President</p>
    <address class="address">
      global traders of minerals<br>
      418 Verandah Heights, Marlow Sector 9<br>
      Dunmore, Kestrel State, 560417.
    </address>
    <ul class="contact">
      <li><b>P :</b>+91-987-654-3217</li>
      <li><b>M :</b>ravi@tessanoverseas.com</li>
    </ul>
    <div class="brand brand--front">
      <span class="brand-dot"></span>
      <span class="brand-name">TESSAN OVERSEAS</span>
    </div>
    <div class="web-band">www.tessanoverseas.com</div>
  </section>

  <section class="card card--back" aria-label="Business card back">
    <div class="brand brand--back">
      <span class="brand-dot"></span>
      <span class="brand-name">TESSAN OVERSEAS</span>
    </div>
  </section>
</main>
</body>
</html>
```